Tolvane Air and Electrical Website

Simple and easy to use website for a Electrical and Air Conditioning contracting business.Use stock photosOnline contact portallogo still to be supplied

Target Market(s)

Mums and Dads who want a local contractor

Coding

Coded - Design and coding required

Number of Pages Required

2 page

Font styles to use
Sans Serif

Colors
f04a50
3276b5
33a6d7

Requirements
Must have
• Simple and easy to use
• Ph number
• 4 web address; linked to page
• 0417385926
• tolvane.com.au
• tolvaneelectrical.com.au
• tolvaneairandelectrical.com.au
• tolvaneair.com.au
Nice to have
• Split System Air Con Picture
• Electrical Pictures

```html
<!DOCTYPE html>
<html lang="en">
<head>
<meta charset="utf-8">
<title>Tolvane Air and Electrical</title>
<link href="https://fonts.googleapis.com/css2?family=Montserrat:wght@400;500;600;700;800&display=swap" rel="stylesheet">
<style>
:root{
  --red:#f04a50;
  --blue:#3276b5;
  --sky:#33a6d7;
  --ink:#222;
  --soft:#f2eeed;
  --dark:#2a2a2a;
  --foot:#2f6fb5;
  --navy:#232a44;
}
*{margin:0;padding:0;box-sizing:border-box}
html,body{width:1200px;height:5329px;overflow:hidden}
body{font-family:'Montserrat',sans-serif;color:var(--ink);background:#fff;position:relative}
section,header,footer{position:absolute;left:0;width:1200px}
.abs{position:absolute}
.ph{position:absolute}

/* header */
.site-header{top:0;height:128px;background:#fff}
.brand{left:132px;top:36px;font-size:40px;font-weight:800;color:var(--blue);letter-spacing:-.5px}
.follow{left:559px;top:36px;font-size:12px;font-weight:600;display:flex;align-items:center;gap:8px}
.follow i{display:inline-block;width:24px;height:24px;border-radius:50%;background:var(--blue)}
.follow i.s{background:var(--sky)}
.follow i.d{background:#1d3f6e}
.call{left:822px;top:20px;display:flex;align-items:center;gap:12px}
.call .sep{width:1px;height:46px;background:#ccc}
.call small{display:block;font-size:12px;font-weight:600}
.call strong{display:block;font-size:28px;font-weight:700;color:var(--blue);line-height:1}
.nav{left:497px;top:93px;font-size:13px;font-weight:600}
.nav a{color:var(--ink);text-decoration:none;position:absolute;white-space:nowrap}
.nav a.on{color:var(--red)}

/* hero */
.hero{top:128px;height:594px;background:linear-gradient(90deg,#f1f2f3 0%,#e3e5e7 45%,#c9cdd1 100%);overflow:hidden}
.hero .scene{left:520px;top:0;width:680px;height:594px;
  background:
    radial-gradient(ellipse 90px 70px at 250px 70px,rgba(232,120,60,.85),rgba(232,120,60,0) 100%),
    radial-gradient(ellipse 110px 120px at 250px 170px,#d9b49a 0%,rgba(217,180,154,0) 100%),
    radial-gradient(ellipse 230px 420px at 250px 440px,#1f2740 0%,#2b3452 55%,rgba(43,52,82,0) 100%),
    radial-gradient(ellipse 70px 40px at 250px 560px,rgba(214,96,40,.9),rgba(214,96,40,0) 100%),
    linear-gradient(90deg,rgba(235,237,239,0) 0%,#b9c0c6 80%,#8e979f 100%)}
.hero h1{left:130px;top:90px;font-size:34px;font-weight:800;color:var(--blue);line-height:42px}
.hero ul{left:130px;top:200px;list-style:none;font-size:15px;line-height:30.3px}
.hero li{display:flex;align-items:center;gap:14px}
.hero li svg{flex:none}
.btn-red{left:130px;top:449px;width:151px;height:44px;background:var(--red);color:#fff;font-weight:700;font-size:15px;display:flex;align-items:center;justify-content:center}
.dots{display:flex;gap:12px;align-items:center}
.dots i{width:10px;height:10px;border-radius:50%;background:#fff;display:block}
.dots i.on{background:var(--red);width:13px;height:13px}
.hero .dots{left:557px;top:538px}

/* services */
.services{top:722px;height:960px;background:var(--soft)}
.sec-title{width:1200px;left:0;text-align:center;font-size:34px;font-weight:800}
.rule{left:579px;width:42px;height:4px;background:#aaa}
.card{width:296px;height:360px;background:#fff;box-shadow:0 2px 6px rgba(0,0,0,.12)}
.card .img{position:absolute;left:0;top:0;width:296px;height:311px}
.card .img::after{content:"";position:absolute;left:0;right:0;bottom:0;height:140px;background:linear-gradient(180deg,rgba(0,0,0,0),rgba(0,0,0,.45))}
.card .label{position:absolute;left:24px;bottom:73px;color:#fff;font-weight:800;font-size:18px;line-height:23px;text-transform:uppercase;z-index:1}
.card .bar{position:absolute;left:0;bottom:0;width:296px;height:49px;display:flex;align-items:center;justify-content:space-between;padding:0 24px;font-size:12px;font-weight:700;color:var(--red)}
.card.feature .img{background:
  radial-gradient(ellipse 120px 90px at 120px 110px,#f3a9a6,rgba(243,169,166,0)),
  radial-gradient(ellipse 80px 110px at 250px 200px,#e68f86,rgba(230,143,134,0)),
  linear-gradient(180deg,#ec6f6e,#d9494b)}
.card.feature .img::after{display:none}
.card.feature .label{bottom:132px}
.card.feature p{position:absolute;left:24px;top:241px;width:210px;color:#fff;font-size:13px;line-height:18px}
.card.feature .bar{background:var(--blue);color:#fff}
.img.install{background:
  radial-gradient(ellipse 90px 50px at 150px 60px,#f5f5f5,rgba(245,245,245,0)),
  radial-gradient(ellipse 30px 40px at 110px 160px,#e1b12c,rgba(225,177,44,0)),
  radial-gradient(ellipse 120px 120px at 210px 260px,#5f6770,rgba(95,103,112,0)),
  linear-gradient(180deg,#dcdcdc,#8d8f92)}
.img.aircon{background:
  linear-gradient(180deg,#f7f7f7 0%,#f1f1f1 22%,#5a6b8a 26%,#e9e9e9 31%,#dcdcdc 100%),
  #e5e5e5}
.img.aircon{background:
  radial-gradient(ellipse 70px 100px at 150px 170px,#c9cbcd,rgba(201,203,205,0)),
  linear-gradient(180deg,#f5f5f5 0%,#eeeeee 20%,#6f7fa0 25%,#e6e6e6 32%,#cfcfcf 100%)}
.img.light{background:
  radial-gradient(ellipse 40px 30px at 90px 200px,#f3c867,rgba(243,200,103,0)),
  radial-gradient(ellipse 50px 30px at 200px 180px,#f0c060,rgba(240,192,96,0)),
  radial-gradient(ellipse 170px 110px at 150px 190px,#d8d6d0,rgba(216,214,208,0)),
  linear-gradient(180deg,#2f3846 0%,#4a5262 55%,#3a3b38 100%)}
.img.outlet{background:
  radial-gradient(ellipse 70px 60px at 90px 130px,#c8c8c8,rgba(200,200,200,0)),
  radial-gradient(ellipse 70px 60px at 200px 130px,#d4d4d4,rgba(212,212,212,0)),
  radial-gradient(ellipse 60px 50px at 70px 40px,#caa088,rgba(202,160,136,0)),
  radial-gradient(ellipse 60px 60px at 260px 200px,#b78f78,rgba(183,143,120,0)),
  linear-gradient(180deg,#8a8a8a,#555)}
.img.wires{background:
  radial-gradient(ellipse 90px 70px at 200px 60px,#6b6f75,rgba(107,111,117,0)),
  radial-gradient(ellipse 110px 60px at 150px 170px,#3c6db5,rgba(60,109,181,0)),
  radial-gradient(ellipse 60px 40px at 170px 210px,#d6b23a,rgba(214,178,58,0)),
  linear-gradient(180deg,#b7bfc8,#4a5563)}

/* why */
.why{top:1682px;height:741px;background:#fff}
.why .photo{left:559px;top:0;width:641px;height:741px;background:
  radial-gradient(ellipse 120px 60px at 350px 60px,#ffffff,rgba(255,255,255,0)),
  radial-gradient(ellipse 90px 110px at 340px 200px,#dcb79c,rgba(220,183,156,0)),
  radial-gradient(ellipse 170px 200px at 330px 420px,#efefef,rgba(239,239,239,0)),
  radial-gradient(ellipse 140px 230px at 470px 500px,#c9353a,rgba(201,53,58,0)),
  radial-gradient(ellipse 150px 120px at 330px 700px,#2d2d30,rgba(45,45,48,0)),
  linear-gradient(90deg,#b7a98a 0%,#8a8d90 20%,#e3e4e5 40%,#c4c7ca 70%,#5c6166 100%)}
.why h2{left:134px;top:42px;font-size:30px;font-weight:500;line-height:36px}
.why h2 b{display:block;font-size:56px;font-weight:800;color:var(--blue);line-height:62px}
.reason{left:130px;width:400px}
.reason .ico{position:absolute;left:0;top:0;width:84px;height:84px;border-radius:50%;background:var(--red);display:flex;align-items:center;justify-content:center}
.reason h3{position:absolute;left:108px;top:4px;font-size:17px;font-weight:600;white-space:nowrap}
.reason p{position:absolute;left:110px;top:34px;width:270px;font-size:12.5px;line-height:19px;color:#555}

/* testimonials */
.testi{top:2423px;height:581px;background:
  linear-gradient(180deg,rgba(47,131,207,0) 60%,rgba(30,90,150,.55) 100%),
  linear-gradient(180deg,#2f83cf,#2a72b8)}
.testi .sec-title{color:#fff}
.quote{width:443px;height:285px;border:2px solid rgba(255,255,255,.85);color:#fff}
.quote .mark{position:absolute;left:40px;top:30px;font-size:50px;font-weight:800;line-height:1}
.quote p{position:absolute;left:74px;top:58px;width:320px;font-size:17px;line-height:24px}
.quote .who{position:absolute;left:74px;top:202px;display:flex;gap:12px;align-items:center}
.quote .av{width:42px;height:42px;border-radius:50%;background:linear-gradient(180deg,#d9c2b0,#3d4a5c);border:2px solid #fff}
.quote .who b{display:block;font-size:12px;font-weight:700}
.quote .who span{font-size:11px;opacity:.85}
.testi .dots{left:558px;top:518px}

/* call reasons */
.why-call{top:3004px;height:1047px;background:#fff}
.why-call .sub{left:0;width:1200px;top:118px;text-align:center;font-size:18px;line-height:27px;color:#333}
.step .num{position:absolute;left:296px;width:70px;height:70px;border-radius:50%;background:var(--blue);color:#fff;font-size:26px;font-weight:700;display:flex;align-items:center;justify-content:center;box-shadow:0 0 0 6px #dbe6f2}
.step h3{position:absolute;left:401px;font-size:17px;font-weight:600;white-space:nowrap}
.step p{position:absolute;left:401px;width:540px;font-size:12.5px;line-height:19px;color:#555}
.dotline{left:330px;top:3279px;width:0;height:633px;border-left:2px dotted var(--blue)}

/* blog */
.blog{top:4051px;height:609px;background:linear-gradient(180deg,#efefef,#fafafa)}
.post{width:290px;height:393px;background:#fff}
.post .img{position:absolute;left:0;top:0;width:290px;height:203px}
.img.panel{background:
  radial-gradient(ellipse 60px 50px at 60px 60px,#e5772e,rgba(229,119,46,0)),
  radial-gradient(ellipse 70px 50px at 230px 110px,#e0742a,rgba(224,116,42,0)),
  radial-gradient(ellipse 120px 80px at 150px 120px,#d7d9dc,rgba(215,217,220,0)),
  linear-gradient(180deg,#3b3f46,#25282d)}
.img.split{background:
  radial-gradient(ellipse 150px 50px at 150px 100px,#ffffff,rgba(255,255,255,0)),
  linear-gradient(180deg,#f1f1f1 0%,#e4e6e8 60%,#9aa0a6 78%,#e9eaeb 100%)}
.img.service{background:
  radial-gradient(ellipse 60px 45px at 90px 60px,#3a4350,rgba(58,67,80,0)),
  radial-gradient(ellipse 40px 40px at 200px 70px,#2a2f38,rgba(42,47,56,0)),
  radial-gradient(ellipse 80px 110px at 210px 160px,#a8d4d6,rgba(168,212,214,0)),
  linear-gradient(180deg,#eef0f2,#d5d9dc)}
.post h3{position:absolute;left:32px;top:226px;width:230px;font-size:17px;font-weight:600;line-height:21px}
.post p{position:absolute;left:32px;top:286px;width:230px;font-size:13px;line-height:19px;color:#555}

/* cta */
.cta{top:4660px;height:332px;background:var(--dark);color:#fff}
.cta p{left:0;width:1200px;top:66px;text-align:center;font-size:27px;font-weight:500;line-height:35px}
.cta .btn{left:441px;top:179px;width:331px;height:87px;background:var(--red);display:flex;align-items:center;gap:16px;padding-left:30px}
.cta .btn small{display:block;font-size:15px;font-weight:700}
.cta .btn strong{display:block;font-size:33px;font-weight:800;line-height:1}

/* footer */
.site-footer{top:4992px;height:337px;background:var(--foot);color:#fff}
.site-footer .brand{left:200px;top:82px;color:#fff;font-size:44px}
.fcol h4{font-size:12px;font-weight:700;margin-bottom:24px}
.fcol{font-size:11px;line-height:18px}
.fcol .row{display:flex;gap:12px;align-items:flex-start;margin-bottom:14px}
.fcol .soc{display:flex;gap:14px;align-items:center;margin-bottom:14px}
.fcol .soc i{width:24px;height:24px;border-radius:50%;background:var(--sky);display:block}
.fcol .soc i.d{background:#1d3f6e}
.copy{left:0;width:1200px;top:292px;text-align:center;font-size:11px}
</style>
</head>
<body>

<header class="site-header">
  <div class="abs brand">Tolvane</div>
  <div class="abs follow">FOLLOW US : <i></i><i class="s"></i><i class="d"></i></div>
  <div class="abs call">
    <svg width="38" height="38" viewBox="0 0 24 24" fill="var(--blue)"><path d="M6.6 10.8a15 15 0 006.6 6.6l2.2-2.2a1 1 0 011-.25 11.4 11.4 0 003.6.57 1 1 0 011 1V20a1 1 0 01-1 1A17 17 0 013 4a1 1 0 011-1h3.5a1 1 0 011 1c0 1.25.2 2.45.57 3.57a1 1 0 01-.25 1z"/></svg>
    <span class="sep"></span>
    <div><small>CALL US</small><strong>0417385926</strong></div>
  </div>
  <nav class="abs nav">
    <a class="on" style="left:0">HOME</a>
    <a style="left:76px">ABOUT US</a>
    <a style="left:190px">SERVICES</a>
    <a style="left:295px">PROJECTS</a>
    <a style="left:409px">BLOG</a>
    <a style="left:480px">CONTACT US</a>
  </nav>
</header>

<section class="hero">
  <div class="ph scene" role="img" aria-label="Smiling electrician in safety glasses and navy overalls with arms crossed, bright workshop behind"></div>
  <h1 class="abs">LOCAL AND TRUSTED<br>ELECTRICAL EXPERTS</h1>
  <ul class="abs">
    <li><svg width="15" height="15" viewBox="0 0 16 16"><circle cx="8" cy="8" r="8" fill="var(--red)"/><path d="M4.5 8.2l2.3 2.3 4.7-4.7" stroke="#fff" stroke-width="2" fill="none"/></svg>Same Day Service</li>
    <li><svg width="15" height="15" viewBox="0 0 16 16"><circle cx="8" cy="8" r="8" fill="var(--red)"/><path d="M4.5 8.2l2.3 2.3 4.7-4.7" stroke="#fff" stroke-width="2" fill="none"/></svg>Over 10 Years of Experience</li>
    <li><svg width="15" height="15" viewBox="0 0 16 16"><circle cx="8" cy="8" r="8" fill="var(--red)"/><path d="M4.5 8.2l2.3 2.3 4.7-4.7" stroke="#fff" stroke-width="2" fill="none"/></svg>Emergency Services Available</li>
    <li><svg width="15" height="15" viewBox="0 0 16 16"><circle cx="8" cy="8" r="8" fill="var(--red)"/><path d="M4.5 8.2l2.3 2.3 4.7-4.7" stroke="#fff" stroke-width="2" fill="none"/></svg>100% Satisfaction Guaranteed</li>
    <li><svg width="15" height="15" viewBox="0 0 16 16"><circle cx="8" cy="8" r="8" fill="var(--red)"/><path d="M4.5 8.2l2.3 2.3 4.7-4.7" stroke="#fff" stroke-width="2" fill="none"/></svg>Licensed, Bonded, and Insured</li>
    <li><svg width="15" height="15" viewBox="0 0 16 16"><circle cx="8" cy="8" r="8" fill="var(--red)"/><path d="M4.5 8.2l2.3 2.3 4.7-4.7" stroke="#fff" stroke-width="2" fill="none"/></svg>Upfront Pricing – No Hidden Fees</li>
    <li><svg width="15" height="15" viewBox="0 0 16 16"><circle cx="8" cy="8" r="8" fill="var(--red)"/><path d="M4.5 8.2l2.3 2.3 4.7-4.7" stroke="#fff" stroke-width="2" fill="none"/></svg>Fees We Offer 15% Off Any Job</li>
  </ul>
  <div class="abs btn-red">READ MORE</div>
  <div class="abs dots"><i></i><i></i><i class="on"></i><i></i><i></i></div>
</section>

<section class="services">
  <h2 class="abs sec-title" style="top:52px">OUR SERVICES</h2>
  <div class="abs rule" style="top:108px"></div>

  <div class="abs card feature" style="left:132px;top:159px">
    <div class="img" role="img" aria-label="Electrician repairing a ceiling smoke detector, red tint"></div>
    <div class="label">Electrical<br>Repair</div>
    <p>Lorem Ipsum is simply dum my text of the printing and typesetting industry.</p>
    <div class="bar">READ MORE <svg width="22" height="16" viewBox="0 0 22 16"><rect x="1" y="1" width="20" height="14" fill="none" stroke="#fff" stroke-width="2"/><path d="M6 8h10M12 4l4 4-4 4" stroke="#fff" stroke-width="2" fill="none"/></svg></div>
  </div>
  <div class="abs card" style="left:453px;top:159px">
    <div class="img install" role="img" aria-label="Technician installing a ceiling vent with a drill"></div>
    <div class="label">Electrical<br>Installation</div>
    <div class="bar">READ MORE <svg width="14" height="10" viewBox="0 0 14 10"><path d="M0 5h12M8 1l4 4-4 4" stroke="var(--red)" stroke-width="2" fill="none"/></svg></div>
  </div>
  <div class="abs card" style="left:772px;top:159px">
    <div class="img aircon" role="img" aria-label="Hand holding a remote below a split system air conditioner"></div>
    <div class="label">Air<br>Conditioning</div>
    <div class="bar">READ MORE <svg width="14" height="10" viewBox="0 0 14 10"><path d="M0 5h12M8 1l4 4-4 4" stroke="var(--red)" stroke-width="2" fill="none"/></svg></div>
  </div>
  <div class="abs card" style="left:132px;top:542px">
    <div class="img light" role="img" aria-label="Modern house with warm lit windows at dusk"></div>
    <div class="label">Indoor &amp; Outdoor<br>Lighting</div>
    <div class="bar">READ MORE <svg width="14" height="10" viewBox="0 0 14 10"><path d="M0 5h12M8 1l4 4-4 4" stroke="var(--red)" stroke-width="2" fill="none"/></svg></div>
  </div>
  <div class="abs card" style="left:453px;top:542px">
    <div class="img outlet" role="img" aria-label="Hands fitting a wall power outlet"></div>
    <div class="label">Switches &amp;<br>Outlets</div>
    <div class="bar">READ MORE <svg width="14" height="10" viewBox="0 0 14 10"><path d="M0 5h12M8 1l4 4-4 4" stroke="var(--red)" stroke-width="2" fill="none"/></svg></div>
  </div>
  <div class="abs card" style="left:772px;top:542px">
    <div class="img wires" role="img" aria-label="Pliers cutting blue and yellow electrical wires"></div>
    <div class="label">Full House<br>Rewire &amp; Wiring<br>Repair</div>
    <div class="bar">READ MORE <svg width="14" height="10" viewBox="0 0 14 10"><path d="M0 5h12M8 1l4 4-4 4" stroke="var(--red)" stroke-width="2" fill="none"/></svg></div>
  </div>
</section>

<section class="why">
  <div class="ph photo" role="img" aria-label="Electrician in white hard hat carrying a red cable coil beside an open white van"></div>
  <h2 class="abs">WHY CHOOSE<b>TOLVANE</b></h2>

  <div class="abs reason" style="top:203px">
    <div class="ico"><svg width="40" height="40" viewBox="0 0 24 24" fill="none" stroke="#fff" stroke-width="2"><path d="M14.7 6.3a4 4 0 005 5L12 19a2.1 2.1 0 01-3-3z"/></svg></div>
    <h3>Responsive repair service</h3>
    <p>Lorem ipsum dolor sit amet, consectetur adipiscing elit, sed do eiusmod tempor incididunt ut labore et dolore.</p>
  </div>
  <div class="abs reason" style="top:319px">
    <div class="ico"><svg width="40" height="40" viewBox="0 0 24 24" fill="none" stroke="#fff" stroke-width="2"><path d="M12 2l8 3v6c0 5-3.5 9-8 11-4.5-2-8-6-8-11V5z"/><path d="M8.5 12l2.5 2.5 4.5-5"/></svg></div>
    <h3>Superior safety practices.</h3>
    <p>Lorem ipsum dolor sit amet, consectetur adipiscing elit, sed do eiusmod tempor incididunt ut labore et dolore.</p>
  </div>
  <div class="abs reason" style="top:443px">
    <div class="ico"><svg width="40" height="40" viewBox="0 0 24 24" fill="#fff"><path d="M2 10h4v11H2zM8 21h9.5a2 2 0 002-1.6l1.4-7A2 2 0 0019 10h-5l.8-4.3A2 2 0 0013 3.4L8 10z"/></svg></div>
    <h3>Highest quality standards</h3>
    <p>Lorem ipsum dolor sit amet, consectetur adipiscing elit, sed do eiusmod tempor incididunt ut labore et dolore.</p>
  </div>
  <div class="abs reason" style="top:576px">
    <div class="ico"><svg width="40" height="40" viewBox="0 0 24 24" fill="none" stroke="#fff" stroke-width="2"><rect x="2" y="5" width="20" height="13" rx="1"/><path d="M6 9h8M6 13h5"/><circle cx="17" cy="14" r="2.5"/></svg></div>
    <h3>Licensed &amp; Certified</h3>
    <p>Lorem ipsum dolor sit amet, consectetur adipiscing elit, sed do eiusmod tempor incididunt ut labore et dolore.</p>
  </div>
</section>

<section class="testi">
  <h2 class="abs sec-title" style="top:52px">TESTIMONIALS</h2>
  <div class="abs rule" style="top:108px;background:#fff"></div>
  <div class="abs quote" style="left:130px;top:176px">
    <div class="mark">“</div>
    <p>Lorem ipsum dolor sit amet conse ctetur adipiscing elit, sed do eiusmod tempor incididunt ut labore et dolore, commodo consequat. Duis aute irure dolor in reprehenderit.</p>
    <div class="who"><div class="av" role="img" aria-label="Customer portrait"></div><div><b>MARCUS</b><span>Bayview</span></div></div>
  </div>
  <div class="abs quote" style="left:627px;top:176px">
    <div class="mark">“</div>
    <p>Lorem ipsum dolor sit amet conse ctetur adipiscing elit, sed do eiusmod tempor incididunt ut labore et dolore, commodo consequat. Duis aute irure dolor in reprehenderit.</p>
    <div class="who"><div class="av" role="img" aria-label="Customer portrait"></div><div><b>MARCUS</b><span>Bayview</span></div></div>
  </div>
  <div class="abs dots"><i></i><i></i><i class="on"></i><i></i><i></i></div>
</section>

<section class="why-call">
  <h2 class="abs sec-title" style="top:62px;font-size:33px">5 REASONS YOU SHOULD CALL US</h2>
  <p class="abs sub">Lorem ipsum dolor sit amet consectetur adipiscing elit<br>sed do eiusmod tempor incididunt ut labore et.</p>
</section>
<div class="abs dotline"></div>
<div class="abs step" style="top:3004px;left:0;width:1200px">
  <div class="num" style="top:240px">1</div>
  <h3 style="top:234px">We do it all.</h3>
  <p style="top:268px">Sed ut perspiciatis unde omnis iste natus error sit voluptatem accusantium doloremque laudantium, totam rem aperiam, eaque ipsa quae ab illo inventore veritatis et quasi architecto beatae vitae dicta sunt explicabo. Nemo enim ipsam voluptatem quia voluptas sit aspernatur aut odit</p>
  <div class="num" style="top:393px">2</div>
  <h3 style="top:387px">Lorem ipsum dolor sit amet, consectetur adipiscing eli</h3>
  <p style="top:421px">Sed ut perspiciatis unde omnis iste natus error sit voluptatem accusantium doloremque laudantium, totam rem aperiam, eaque ipsa quae ab illo inventore veritatis et quasi architecto beatae vitae dicta sunt explicabo. Nemo enim ipsam voluptatem quia voluptas sit aspernatur aut odit</p>
  <div class="num" style="top:551px">3</div>
  <h3 style="top:545px">But I must explain to you how all this mistaken idea</h3>
  <p style="top:579px">Sed ut perspiciatis unde omnis iste natus error sit voluptatem accusantium doloremque laudantium, totam rem aperiam, eaque ipsa quae ab illo inventore veritatis et quasi architecto beatae vitae dicta sunt explicabo. Nemo enim ipsam voluptatem quia voluptas sit aspernatur aut odit</p>
  <div class="num" style="top:710px">4</div>
  <h3 style="top:704px">Lorem ipsum dolor sit amet, consectetur adipiscing eli</h3>
  <p style="top:738px">Sed ut perspiciatis unde omnis iste natus error sit voluptatem accusantium doloremque laudantium, totam rem aperiam, eaque ipsa quae ab illo inventore veritatis et quasi architecto beatae vitae dicta sunt explicabo. Nemo enim ipsam voluptatem quia voluptas sit aspernatur aut odit</p>
  <div class="num" style="top:873px">5</div>
  <h3 style="top:867px">But I must explain to you how all this mistaken idea</h3>
  <p style="top:901px">Sed ut perspiciatis unde omnis iste natus error sit voluptatem accusantium doloremque laudantium, totam rem aperiam, eaque ipsa quae ab illo inventore veritatis et quasi architecto beatae vitae dicta sunt explicabo. Nemo enim ipsam voluptatem quia voluptas sit aspernatur aut odit</p>
</div>

<section class="blog">
  <h2 class="abs sec-title" style="top:48px">LATEST BLOG</h2>
  <article class="abs post" style="left:132px;top:157px">
    <div class="img panel" role="img" aria-label="Orange gloved hands working on a circuit breaker panel"></div>
    <h3>Lorem ipsum dolor sit amet consectetur</h3>
    <p>Sed ut perspiciatis unde omnis iste natus error sit voluptatem accusantium doloremque laudantium</p>
  </article>
  <article class="abs post" style="left:455px;top:157px">
    <div class="img split" role="img" aria-label="White split system air conditioner on a wall"></div>
    <h3>Lorem ipsum dolor sit amet consectetur</h3>
    <p>Sed ut perspiciatis unde omnis iste natus error sit voluptatem accusantium doloremque laudantium</p>
  </article>
  <article class="abs post" style="left:778px;top:157px">
    <div class="img service" role="img" aria-label="Technician servicing a wall air conditioning unit"></div>
    <h3>Lorem ipsum dolor sit amet consectetur</h3>
    <p>Sed ut perspiciatis unde omnis iste natus error sit voluptatem accusantium doloremque laudantium</p>
  </article>
</section>

<section class="cta">
  <p class="abs">Sed ut perspiciatis unde omnis iste natus error sit<br>voluptatem accusantium doloremque lau.</p>
  <div class="abs btn">
    <svg width="46" height="46" viewBox="0 0 24 24" fill="none" stroke="#fff" stroke-width="1.8"><path d="M6.6 10.8a15 15 0 006.6 6.6l2.2-2.2a1 1 0 011-.25 11.4 11.4 0 003.6.57 1 1 0 011 1V20a1 1 0 01-1 1A17 17 0 013 4a1 1 0 011-1h3.5a1 1 0 011 1c0 1.25.2 2.45.57 3.57a1 1 0 01-.25 1z"/></svg>
    <div><small>CALL US</small><strong>0417385926</strong></div>
  </div>
</section>

<footer class="site-footer">
  <div class="abs brand">Tolvane</div>
  <div class="abs fcol" style="left:492px;top:48px">
    <h4>CONTACT US</h4>
    <div class="row"><svg width="10" height="14" viewBox="0 0 10 14" fill="#fff"><path d="M5 0a5 5 0 015 5c0 3.5-5 9-5 9S0 8.5 0 5a5 5 0 015-5zm0 3a2 2 0 100 4 2 2 0 000-4z"/></svg><span>3817 Wren Avenue<br>Marlow, CA 91802</span></div>
    <div class="row"><svg width="12" height="12" viewBox="0 0 24 24" fill="#fff"><path d="M6.6 10.8a15 15 0 006.6 6.6l2.2-2.2a1 1 0 011-.25 11.4 11.4 0 003.6.57 1 1 0 011 1V20a1 1 0 01-1 1A17 17 0 013 4a1 1 0 011-1h3.5a1 1 0 011 1c0 1.25.2 2.45.57 3.57a1 1 0 01-.25 1z"/></svg><span>0417385926</span></div>
    <div class="row" style="margin-top:20px"><svg width="13" height="10" viewBox="0 0 13 10"><rect width="13" height="10" fill="#fff"/><path d="M0 0l6.5 5L13 0" stroke="var(--foot)" fill="none"/></svg><span>info@tolvane.com.au</span></div>
  </div>
  <div class="abs fcol" style="left:763px;top:48px">
    <h4>MENU</h4>
    <div>HOME<br>ABOUT US<br>SERVICES<br>PROJECTS<br>BLOG<br>CONTACT US</div>
  </div>
  <div class="abs fcol" style="left:950px;top:48px">
    <h4>CONNECT WITH US</h4>
    <div class="soc"><i></i><span>Community</span></div>
    <div class="soc" style="margin-top:16px"><i></i><span>Updates</span></div>
    <div class="soc" style="margin-top:16px"><i class="d"></i><span>Network</span></div>
  </div>
  <div class="abs copy">Copyrights @ 2019 All Rights Reserved</div>
</footer>

</body>
</html>
```